Stationary pack
Stationary
Project: Stationary pack
Stationary pack - Construction
Creative Brief
Simple
Derek Olsworth
318 Harrowdene Lane Stoketon Marlbridge Wendshire ME7 4RB
brightlinejoiner@mailvane.net

```html
<!DOCTYPE html>
<html lang="en">
<head>
<meta charset="utf-8">
<title>Derek Olsworth – Business Card</title>
<link rel="stylesheet" href="https://fonts.googleapis.com/css2?family=Open+Sans:wght@400;600&display=swap">
<style>
  :root {
    --blue: #1e6fc2;
    --grey-light: #c9ccd0;
    --ink: #5b6068;
    --card: #ffffff;
    --bg: #eceef1;
  }
  * { margin: 0; padding: 0; box-sizing: border-box; }
  html, body { width: 1200px; height: 701px; overflow: hidden; }
  body {
    background: var(--bg);
    font-family: "Open Sans", Arial, sans-serif;
    position: relative;
  }
  .card {
    position: absolute;
    top: 190px;
    width: 520px;
    height: 320px;
    background: var(--card);
    border-radius: 16px;
    overflow: hidden;
    box-shadow: 0 6px 18px rgba(0,0,0,0.12);
  }
  .card--front {
    left: 50px;
    border: 8px solid var(--blue);
    box-shadow: inset 0 0 0 6px var(--grey-light), 0 6px 18px rgba(0,0,0,0.12);
  }
  .card--back { left: 630px; }

  .brand {
    display: flex;
    align-items: center;
    gap: 12px;
    color: var(--blue);
    font-weight: 600;
    text-transform: uppercase;
    line-height: 1.15;
    white-space: nowrap;
  }
  .brand__mark {
    background: var(--blue);
    flex: none;
  }
  .card--front .brand {
    position: absolute;
    left: 50%;
    top: 50%;
    transform: translate(-50%, -50%);
    font-size: 22px;
    letter-spacing: 1px;
  }
  .card--front .brand__mark { width: 52px; height: 52px; }

  .card--back .brand {
    position: absolute;
    left: 30px;
    top: 34px;
    font-size: 14px;
    letter-spacing: 0.5px;
    gap: 9px;
  }
  .card--back .brand__mark { width: 34px; height: 34px; }

  .contact {
    position: absolute;
    left: 30px;
    top: 160px;
    list-style: none;
    font-size: 11px;
    color: var(--ink);
  }
  .contact li { display: flex; align-items: center; gap: 7px; margin-bottom: 7px; }
  .contact svg { width: 10px; height: 10px; fill: var(--blue); }

  .person {
    position: absolute;
    right: 34px;
    top: 166px;
    text-align: right;
    width: 250px;
  }
  .person__name {
    font-size: 22px;
    font-weight: 400;
    color: var(--blue);
    padding-bottom: 6px;
    border-bottom: 1px solid var(--grey-light);
    margin-bottom: 8px;
  }
  .person__address {
    font-style: normal;
    font-size: 11.5px;
    color: var(--ink);
    line-height: 1.6;
  }
  .band {
    position: absolute;
    left: 0;
    bottom: 0;
    width: 520px;
    height: 70px;
  }
</style>
</head>
<body>
  <section class="card card--front" aria-label="Card front">
    <div class="brand">
      <span class="brand__mark"></span>
      <span>Derek Olsworth<br>Kitchen Fitter</span>
    </div>
  </section>

  <section class="card card--back" aria-label="Card back">
    <div class="brand">
      <span class="brand__mark"></span>
      <span>Derek Olsworth<br>Kitchen Fitter</span>
    </div>

    <ul class="contact">
      <li>
        <svg viewBox="0 0 10 10"><path d="M2 0h2l1 2.5-1.3 1a6 6 0 0 0 2.8 2.8l1-1.3L10 6v2a2 2 0 0 1-2 2A8 8 0 0 1 0 2a2 2 0 0 1 2-2z"/></svg>
        07482 615209
      </li>
      <li>
        <svg viewBox="0 0 10 10"><path d="M0 2h10v6H0z M0 2l5 3.5L10 2" /></svg>
        brightlinejoiner@mailvane.net
      </li>
    </ul>

    <div class="person">
      <h1 class="person__name">Derek Olsworth</h1>
      <address class="person__address">318 Harrowdene Lane<br>Stoketon, Marlbridge, Wendshire ME7 4RB</address>
    </div>

    <svg class="band" viewBox="0 0 520 70" preserveAspectRatio="none" aria-hidden="true">
      <path d="M0 40 H280 C330 40 340 18 390 18 H520 V70 H0 Z" fill="var(--grey-light)"/>
      <path d="M0 46 H290 C340 46 350 26 400 26 H520 V70 H0 Z" fill="var(--blue)"/>
    </svg>
  </section>
</body>
</html>
```